Finance Broker helping people meet their personal and business goals

New business card design,
1st look at the old business card so this makes sense.
I DON'T want:
the subtext "For all your Rural and Commercial Finance".
I DON'T want the: "and Management Consultant" words
I DON'T want the old phone: 07 49217305
I DON'T want the fax number: 07 48160923
I DON'T want the email address: tallowcreek@quarnet.com.au
I DON'T want the flower
What I DO want
I DO want the mobile 0418 365 907 (in larger text)
I DO want:
My name: Dennis Harlow-Pike
I DO want: Australian Credit Licence 512964 (Tallow Creek Pty Ltd)
I DO want: Principal Finance Broker
I DO want new email: dennis@plantreasurepath.com.au
I DO want address: PO Box 836, Marrowbank Qld 4872
I DO want the existing logo (PTP on existing card)

Target Market(s)

Business Borrowers, Home Purchasers, and People wanting to finance cars and plant and equipment

Industry/Entity Type

Financial Service

Contact Information for Business Card

See project description

Font styles to use
Serif

Colors

Designer to choose colors to be used in the design.

Requirements
Must have
• See project description
Nice to have
• Black and Yellow colours
Should not have
• See project description

```html
<!DOCTYPE html>
<html lang="en">
<head>
<meta charset="utf-8">
<title>Plan Treasure Path – Business Card</title>
<link rel="stylesheet" href="https://fonts.googleapis.com/css2?family=Lato:wght@400;700&display=swap">
<style>
  :root {
    --page: #ffffff;
    --card: #222222;
    --accent: #f7ec8a;
    --ink-light: #ffffff;
  }
  html, body {
    margin: 0;
    padding: 0;
    width: 1000px;
    height: 1200px;
    overflow: hidden;
    background: var(--page);
  }
  .canvas {
    position: relative;
    width: 1000px;
    height: 1200px;
    font-family: "Lato", Arial, sans-serif;
  }
  .business-card {
    position: absolute;
    left: 54px;
    top: 344px;
    width: 891px;
    height: 513px;
    background: var(--card);
    box-shadow: 0 6px 22px rgba(0, 0, 0, 0.45);
    color: var(--ink-light);
    text-align: center;
  }
  .card-strip {
    position: absolute;
    left: 0;
    bottom: 0;
    width: 100%;
    height: 11px;
    background: var(--accent);
  }
  .line {
    position: absolute;
    left: 0;
    width: 100%;
    margin: 0;
    line-height: 1;
    white-space: nowrap;
  }
  .brand {
    top: 42px;
    display: flex;
    justify-content: center;
    align-items: center;
  }
  .brand-mark {
    width: 88px;
    height: 88px;
  }
  .brand-name {
    top: 142px;
    font-size: 44px;
    font-weight: 400;
    color: var(--accent);
  }
  .brand-group {
    top: 193px;
    font-size: 21px;
  }
  .mobile {
    top: 244px;
    font-size: 36px;
    font-weight: 700;
  }
  .person-name {
    top: 302px;
    font-size: 26px;
    font-weight: 700;
    color: var(--accent);
  }
  .licence {
    top: 337px;
    font-size: 22px;
  }
  .role {
    top: 370px;
    font-size: 22px;
  }
  .email {
    top: 421px;
    font-size: 22px;
  }
  .address {
    top: 452px;
    font-size: 22px;
  }
  .label {
    font-weight: 700;
    color: var(--accent);
  }
</style>
</head>
<body>
<div class="canvas">
  <section class="business-card">
    <div class="line brand">
      <svg class="brand-mark" viewBox="0 0 88 88" aria-hidden="true">
        <circle cx="44" cy="44" r="44" fill="var(--accent)"/>
      </svg>
    </div>
    <p class="line brand-name">Plan Treasure Path</p>
    <p class="line brand-group">A Member of the Tallow Creek Group</p>

    <p class="line mobile">0418 365 907</p>

    <p class="line person-name">Dennis Harlow-Pike</p>
    <p class="line licence">Australian Credit Licence 512964 (Tallow Creek Pty Ltd)</p>
    <p class="line role">Principal Finance Broker</p>

    <p class="line email"><span class="label">Email:</span> dennis@plantreasurepath.com.au</p>
    <p class="line address"><span class="label">Address:</span> PO Box 836, Marrowbank Qld 4872</p>

    <div class="card-strip"></div>
  </section>
</div>
</body>
</html>
```